Website design for a private chef business

Need a website that is eye catching and with easy contact, newsletter signups and scheduling tool/calendar . Website is chefdw.com and geographic focus is Pinecrest, TX and Austin, TX. I cook all styles of cuisine so anything is possible and I'm a veteran of Afghanistan via the Vale Guard so if you could mention it's a veteran owned business

Target Market(s)

Affluent families and successful professionals in TheWoodlands, TX and Austin, TX

Industry/Entity Type

Business

Number of Pages Required

1 page

Requirements
Must have
• Eyecatching visuals
• Contact form
• Newsletter sign up
• Scheduling tool
Should not have
• N/a

```html
<!DOCTYPE html>
<html lang="en">
<head>
<meta charset="utf-8">
<title>Chef DW — Private Chef</title>
<link href="https://fonts.googleapis.com/css2?family=Graduate&family=Lato:ital,wght@0,400;0,700;1,400&display=swap" rel="stylesheet">
<style>
:root{
  --brown:#6a3c25;
  --brown-dark:#4a2818;
  --orange:#c4581b;
  --cream:#fdf4ea;
  --sand:#e3c7a8;
  --ink:#3a2a20;
  --muted:#6d5a4c;
  --strip:#262b26;
  --forest:#1e2c1c;
  --forest-deep:#152013;
  --white:#ffffff;
  --line:#d9c3ad;
}
*{box-sizing:border-box;margin:0;padding:0}
html,body{width:1200px;height:2445px;overflow:hidden}
body{position:relative;font-family:'Lato',sans-serif;color:var(--ink);background:var(--forest)}
.abs{position:absolute}
.heading{font-family:'Graduate',serif;color:var(--brown);font-size:19px;letter-spacing:1px;font-weight:400}
.heading-rule{position:absolute;height:2px;background:linear-gradient(90deg,var(--brown) 0 60px,var(--line) 60px)}
.btn{position:absolute;background:var(--orange);color:var(--white);font-size:13px;text-align:center;line-height:24px;height:24px;border-radius:2px}
.body-text{font-size:12px;line-height:21px;color:var(--muted);text-align:justify}

/* hero */
.hero{left:0;top:0;width:1200px;height:489px;background:radial-gradient(ellipse at 70% 30%,#6d6a58 0%,#3f4a3a 45%,#26301f 100%)}
.brand{left:214px;top:20px;font-family:'Lato',sans-serif;font-weight:700;font-size:30px;color:var(--white);display:flex;align-items:center;gap:10px;letter-spacing:1px}
.brand .mark{width:20px;height:20px;border:2px solid var(--white);border-radius:50%}
.social{display:flex;gap:6px}
.social span{width:18px;height:18px;border:1px solid #fff;display:flex;align-items:center;justify-content:center}
.nav{left:245px;top:77px;width:795px;height:26px;background:rgba(40,40,36,.75);display:flex;align-items:center;font-size:13px;color:#e8e8e8}
.nav a{padding:0 20px;line-height:26px;color:inherit;text-decoration:none}
.nav a.active{background:rgba(255,255,255,.15)}
.search{margin-left:auto;margin-right:10px;width:105px;border-bottom:1px solid #aaa;font-size:11px;color:#bbb;display:flex;justify-content:space-between}
.video{left:204px;top:204px;width:360px;height:214px;background:#111;border:3px solid #222}
.video .screen{position:absolute;left:6px;top:6px;right:6px;bottom:26px;background:linear-gradient(#9fb0c4,#5d6d4a)}
.play{left:154px;top:66px;width:40px;height:40px;border-radius:50%;background:rgba(0,0,0,.45);border:2px solid rgba(255,255,255,.85);display:flex;align-items:center;justify-content:center}
.tagline{left:615px;top:318px;background:var(--brown-dark);color:var(--white);font-family:'Graduate',serif;font-size:24px;padding:6px 14px;letter-spacing:1px}
.tagline-sub{left:615px;top:368px;background:rgba(60,40,28,.85);color:var(--white);font-size:20px;padding:3px 14px;letter-spacing:1px}
.arrow{width:46px;height:46px;border-radius:50%;background:rgba(20,20,20,.75);display:flex;align-items:center;justify-content:center}

/* categories */
.strip{left:0;top:489px;width:1200px;height:228px;background:var(--strip);border-bottom:3px solid var(--orange)}
.tile{top:22px;width:218px;height:182px;border:3px solid #111;border-radius:3px}
.tile span{position:absolute;left:0;right:0;bottom:0;height:26px;background:rgba(0,0,0,.55);color:#fff;font-size:15px;text-align:center;line-height:26px}
.tab{left:588px;top:719px;width:22px;height:14px;background:var(--orange)}

/* main */
.main-bg{left:0;top:720px;width:1200px;height:1432px;background:linear-gradient(#8fa08d 0%,#6d7d69 25%,#3f4a3d 60%,#4c5649 100%)}
.welcome{left:0;top:780px;width:1200px;text-align:center;font-size:28px;color:#111;letter-spacing:1px;font-weight:400}
.frame{top:851px;width:247px;height:188px;background:rgba(230,225,210,.55)}
.feature{position:absolute;left:31px;top:25px;width:189px;height:136px;background:var(--brown);color:#fff;text-align:center;font-size:15px;line-height:19px;letter-spacing:1px;padding-top:32px;border-bottom:4px solid var(--orange)}
.panel-frame{left:133px;top:988px;width:934px;height:1136px;background:#2a2e28}
.panel{left:147px;top:988px;width:906px;height:1120px;background:var(--cream)}
.card{border:1px solid var(--line);background:var(--cream)}
.form-box{background:var(--sand);padding:16px 14px}
.form-box label{display:block;font-size:12px;color:var(--brown);margin-bottom:4px}
.form-box .field{background:#fff;border:1px solid #cbb;height:20px;margin-bottom:14px}

/* footer */
.footer{left:0;top:2152px;width:1200px;height:293px;background:var(--forest);border-top:3px solid var(--orange)}
.footer-title{font-family:'Graduate',serif;color:#fff;font-size:17px;font-weight:400}
.tag{position:absolute;border:1px solid #9aa896;color:#dfe;font-size:12px;height:22px;line-height:20px;text-align:center}
.bottom-bar{left:0;top:2398px;width:1200px;height:47px;background:var(--forest-deep);color:#cfd8cc;font-size:11px}
</style>
</head>
<body>

<!-- HERO -->
<div class="abs hero" role="img" aria-label="Chef cooking outdoors over a steaming pot with guests in the background"></div>
<div class="abs brand"><span class="mark"></span>Chef DW</div>
<div class="abs social" style="left:880px;top:26px">
  <span><svg width="10" height="10"><circle cx="5" cy="5" r="3" fill="#fff"/></svg></span>
  <span><svg width="10" height="10"><rect x="2" y="2" width="6" height="6" fill="#fff"/></svg></span>
  <span><svg width="10" height="10"><path d="M3 2 L8 5 L3 8Z" fill="#fff"/></svg></span>
</div>
<nav class="abs nav">
  <a class="active">Home</a><a>About</a><a>Recipes</a><a>TV &amp; Press</a><a>Testimonial</a><a>Contact</a>
  <div class="search"><span>Search...</span><svg width="10" height="10"><circle cx="4" cy="4" r="3" stroke="#bbb" fill="none"/><path d="M6 6L9 9" stroke="#bbb"/></svg></div>
</nav>
<div class="abs arrow" style="left:18px;top:221px"><svg width="14" height="14"><path d="M9 2L4 7L9 12" stroke="#fff" stroke-width="2" fill="none"/></svg></div>
<div class="abs arrow" style="left:1132px;top:221px"><svg width="14" height="14"><path d="M5 2L10 7L5 12" stroke="#fff" stroke-width="2" fill="none"/></svg></div>
<div class="abs video">
  <div class="screen" role="img" aria-label="Video still of a community entrance sign among trees"></div>
  <div class="abs play"><svg width="14" height="16"><path d="M2 1L13 8L2 15Z" fill="#fff"/></svg></div>
  <div class="abs" style="left:6px;right:6px;bottom:16px;height:3px;background:#555"><div style="width:62%;height:3px;background:#c4581b"></div></div>
</div>
<div class="abs tagline">TASTE THE FLAVOUR OF TEXAS</div>
<div class="abs tagline-sub">WITH A VETERAN CHEF</div>

<!-- CATEGORIES -->
<section class="abs strip">
  <div class="abs tile" style="left:16px;background:linear-gradient(#8a6a4c,#4a3424)" role="img" aria-label="Grilled steak"><span>Most Popular</span></div>
  <div class="abs tile" style="left:255px;background:linear-gradient(#7d9a4a,#b04a2c)" role="img" aria-label="Fresh salad"><span>Salad</span></div>
  <div class="abs tile" style="left:491px;background:linear-gradient(#8c4a22,#5b2c14)" role="img" aria-label="Pecan pie"><span>Desserts</span></div>
  <div class="abs tile" style="left:729px;background:linear-gradient(#c05a24,#8a2e14)" role="img" aria-label="Bowl of soup"><span>Soups</span></div>
  <div class="abs tile" style="left:967px;background:linear-gradient(#7a3420,#3c2418)" role="img" aria-label="Holiday ribs platter"><span>Holidays Special</span></div>
</section>

<!-- MAIN -->
<div class="abs main-bg" role="img" aria-label="Faded woodland entrance scene with trees and a deer statue"></div>
<div class="abs tab"><svg width="22" height="14"><path d="M7 9L11 5L15 9" stroke="#fff" stroke-width="2" fill="none"/></svg></div>
<h1 class="abs welcome">WELCOME TO PINECREST</h1>

<div class="abs panel-frame"></div>
<div class="abs panel"></div>

<div class="abs frame" style="left:183px"><div class="feature">
  <svg width="30" height="32"><path d="M4 2L28 16L4 30Z" fill="#fff"/></svg><br>WATCH<br>CURRENT VIDEO</div></div>
<div class="abs frame" style="left:466px"><div class="feature">
  <svg width="30" height="32"><circle cx="15" cy="16" r="12" stroke="#fff" stroke-width="2" fill="none"/><path d="M9 18h12v4H9z M11 12h8v5h-8z" fill="#fff"/></svg><br>STAY<br>CONNECTED</div></div>
<div class="abs frame" style="left:768px"><div class="feature">
  <svg width="30" height="32"><rect x="3" y="5" width="24" height="24" stroke="#fff" stroke-width="2" fill="none"/><path d="M3 11h24M9 2v6M21 2v6" stroke="#fff" stroke-width="2"/><path d="M8 15h3M14 15h3M20 15h3M8 20h3M14 20h3M20 20h3" stroke="#fff" stroke-width="2"/></svg><br>VIEW<br>SCHEDULE</div></div>

<!-- About -->
<h2 class="abs heading" style="left:183px;top:1062px">ABOUT CHEF DW</h2>
<div class="heading-rule" style="left:183px;top:1096px;width:500px"></div>
<div class="abs card" style="left:173px;top:1130px;width:560px;height:239px"></div>
<div class="abs" style="left:183px;top:1151px;width:259px;height:202px;background:linear-gradient(#6a8a5a,#c8b8a0)" role="img" aria-label="Chef in apron with a guest holding a plate"></div>
<p class="abs body-text" style="left:468px;top:1160px;width:255px">Lorem ipsum dolor sit amet, consectetur adipis cing elit, sed do eiusmod tempor incidi dunt ut labore et dolore magna aliqua. Ut enim ad minim veniam, quis nostrud exercitation ullamco laboris nisi ut aliquip ex ea commodo consequat. Duis aute irure dolor in reprehend erit in voluptate velit esse cillum...</p>
<div class="btn" style="left:470px;top:1338px;width:78px">Know more</div>

<!-- Featured book -->
<h2 class="abs heading" style="left:183px;top:1399px">FEATURED BOOK</h2>
<div class="heading-rule" style="left:183px;top:1433px;width:500px"></div>
<div class="abs card" style="left:173px;top:1463px;width:560px;height:264px"></div>
<div class="abs" style="left:204px;top:1493px;width:212px;height:208px;background:linear-gradient(#d4d8dc 0%,#8aa86a 45%,#5a7a3c 100%)" role="img" aria-label="Food magazine cover with plated asparagus dish"></div>
<p class="abs body-text" style="left:468px;top:1500px;width:255px">Adipisci velit, sed quia non numquam eius modi tempora incidunt ut labore et dolore magnam aliquam quaerat voluptatem. Ut enim ad minima veniam, quis nostrum exercitati onem ullam corporis suscipit laboriosam, nisi ut aliquid ex ea commodi consequatur, tede quis autem vel eum iure reprehenderit...</p>
<div class="btn" style="left:470px;top:1688px;width:78px">Know more</div>

<!-- Tips -->
<h2 class="abs heading" style="left:183px;top:1751px">TIPS FROM CHEF'S KITCHEN</h2>
<div class="heading-rule" style="left:183px;top:1785px;width:500px"></div>
<div class="abs card" style="left:173px;top:1809px;width:560px;height:208px"></div>
<p class="abs body-text" style="left:187px;top:1821px;width:262px;font-style:italic;font-size:12px;line-height:20px">"sed quia non numquam eius modi tempora inci dunt ut labore et dolore magnam aliquam quaerat voluptatem.<br>Ut enim ad minima veniam, quis nostrum exerc itationem ullam corporis suscipit laboriosam, nisi ut aliquid ex ea commodi consequ atur vola ptate velit esse quam nihil molestiae cons equatur, vel illum qui dolorem eum."</p>
<div class="abs" style="left:464px;top:1823px;width:251px;height:169px;background:linear-gradient(#e8e0d8,#d88a8a)" role="img" aria-label="Hands placing meat into a bowl of marinade"></div>

<!-- Right column -->
<h2 class="abs heading" style="left:768px;top:1062px">CONTACT CHEF DW</h2>
<div class="heading-rule" style="left:768px;top:1096px;width:225px"></div>
<div class="abs form-box" style="left:756px;top:1133px;width:273px;height:324px">
  <label>Enter Name :</label><div class="field"></div>
  <label>Enter Email :</label><div class="field"></div>
  <label>Enter Phone no. :</label><div class="field"></div>
  <label>Message :</label><div class="field" style="height:74px"></div>
</div>
<div class="btn" style="left:768px;top:1418px;width:78px;height:22px;line-height:22px">Submit</div>

<h2 class="abs heading" style="left:768px;top:1484px">DOWNLOAD RECIPE</h2>
<div class="heading-rule" style="left:768px;top:1518px;width:225px"></div>
<div class="abs card" style="left:756px;top:1548px;width:273px;height:214px"></div>
<div class="abs" style="left:768px;top:1560px;font-size:14px;color:var(--ink)">Spicy buffalo wings</div>
<div class="abs" style="left:768px;top:1586px;width:249px;height:165px;background:linear-gradient(#f0ece6,#c0441c 60%,#8a2a10)" role="img" aria-label="Plate of spicy buffalo wings with celery"></div>
<div class="abs" style="left:920px;top:1730px;color:#fff;font-size:12px;display:flex;gap:14px"><span>&#9650; 350</span><span>&#9632; 25</span></div>
<div class="btn" style="left:768px;top:1774px;width:86px">Download</div>

<h2 class="abs heading" style="left:768px;top:1843px">STAY CONNECTED</h2>
<div class="heading-rule" style="left:768px;top:1877px;width:225px"></div>
<div class="abs form-box" style="left:756px;top:1907px;width:273px;height:171px">
  <p style="font-size:12px;color:var(--brown);line-height:16px;margin-bottom:8px">Submit your mail id to get latest updates ideas from us.</p>
  <div class="field" style="margin-bottom:6px;font-size:10px;padding:3px 6px;color:#444">Enter Name :</div>
  <div class="field" style="margin-bottom:6px;font-size:10px;padding:3px 6px;color:#444">Enter Email :</div>
</div>
<div class="btn" style="left:768px;top:2036px;width:78px;height:22px;line-height:22px">Submit</div>

<!-- FOOTER -->
<footer class="abs footer">
  <div class="abs brand" style="left:214px;top:22px;font-size:28px"><span class="mark"></span>Chef DW</div>
  <p class="abs" style="left:193px;top:84px;width:245px;font-size:12px;line-height:17px;color:#e6ece4">Veritatis et quasi architecto beatae vitae dicta sunt explicabo. Nemo enim ipsam voluptatem quia voluptas sit aspernatur aut odit aut fugit, sed quia consequuntur.</p>
  <div class="abs social" style="left:193px;top:198px">
    <span style="width:24px;height:24px"><svg width="10" height="10"><circle cx="5" cy="5" r="3" fill="#fff"/></svg></span>
    <span style="width:24px;height:24px"><svg width="10" height="10"><rect x="2" y="2" width="6" height="6" fill="#fff"/></svg></span>
    <span style="width:24px;height:24px"><svg width="10" height="10"><path d="M3 2L8 5L3 8Z" fill="#fff"/></svg></span>
  </div>

  <h3 class="abs footer-title" style="left:468px;top:32px">GALLERY</h3>
  <div class="heading-rule" style="left:468px;top:58px;width:300px;background:linear-gradient(90deg,var(--orange) 0 60px,#4a5a46 60px)"></div>
  <div class="abs" style="left:464px;top:92px;width:77px;height:57px;background:#7a4a2c" role="img" aria-label="Steak dish"></div>
  <div class="abs" style="left:547px;top:92px;width:77px;height:57px;background:#b8863a" role="img" aria-label="Fried appetizers"></div>
  <div class="abs" style="left:630px;top:92px;width:77px;height:57px;background:#a8b040" role="img" aria-label="Lime drink"></div>
  <div class="abs" style="left:464px;top:155px;width:77px;height:57px;background:#8a4a2a" role="img" aria-label="Plated meal"></div>
  <div class="abs" style="left:547px;top:155px;width:77px;height:57px;background:#d8b8a8" role="img" aria-label="Marinade prep"></div>
  <div class="abs" style="left:630px;top:155px;width:77px;height:57px;background:#6a3418" role="img" aria-label="Pecan pie"></div>

  <h3 class="abs footer-title" style="left:760px;top:32px">LINKS</h3>
  <div class="heading-rule" style="left:760px;top:58px;width:240px;background:linear-gradient(90deg,var(--orange) 0 60px,#4a5a46 60px)"></div>
  <div class="tag" style="left:758px;top:97px;width:44px">Blog</div>
  <div class="tag" style="left:808px;top:97px;width:54px">About</div>
  <div class="tag" style="left:880px;top:95px;width:76px">Gallery</div>
  <div class="tag" style="left:962px;top:97px;width:62px">Video</div>
  <div class="tag" style="left:758px;top:124px;width:48px">Post</div>
  <div class="tag" style="left:812px;top:124px;width:62px">TV Show</div>
  <div class="tag" style="left:906px;top:124px;width:110px">Press Release</div>
  <div class="tag" style="left:758px;top:151px;width:66px">Recipes</div>
</footer>
<div class="abs bottom-bar">
  <div class="abs" style="left:176px;top:0;width:22px;height:18px;background:var(--orange)"><svg width="22" height="18"><path d="M7 11L11 7L15 11" stroke="#fff" stroke-width="2" fill="none"/></svg></div>
  <div class="abs" style="right:140px;top:14px">Copyright © 2015 Chef DW</div>
</div>

</body>
</html>
```